Healthy lifestyle Influencer business card

I need your creativity to have a business card that I can leave in all the restaurants, hotels and spas I visit to inform them that I am an influencer specializing in the wellness sector and that I will write a review about them. You can use my instagram photos Velusport72 or on my website www.piattileggerinuovi.it. I would like my business card to impress with its creativity! thank you very much!

Contact Information for Business Card

siteweb, instagram, phone number

Font styles to use
Decorative
Script

Colors
0094D4
00A9DD
6FCCEA
C7EBF8
E9F6FB
59FF00
82FF00
B8FF75
E3FFCB
F4FFEA
FFC000
F8CF3A
FAE287
FDF2CF
FEFAEE
F0912C
F2A743
F7CA91
FBE8D2
FDF5EE
EE7325
F08F49
F5BC92
FAE3D3
FDF4ED
EB3D1F
EC4F4E
F09395
F8D3D4
FCEDEE
E54698
E96AAD
F1A4CE
F9D9EA
FCEFF6

Requirements
Nice to have
• creativity

```html
<!DOCTYPE html>
<html lang="it">
<head>
<meta charset="utf-8">
<title>Lieve Cucina – Business Card</title>
<link href="https://fonts.googleapis.com/css2?family=Montserrat:wght@400;500;700&display=swap" rel="stylesheet">
<style>
  :root {
    --stage: #333333;
    --card-white: #ffffff;
    --card-grey: #666666;
    --ink: #4a4a4a;
    --ink-soft: #5c5c5c;
    --accent: #f2a743;
    --peach: #f5dcc3;
    --band-dark: #4d4d4d;
    --silver: #d9d9d9;
    --rule: #6b6b6b;
  }
  * { box-sizing: border-box; margin: 0; padding: 0; }
  html, body { width: 1200px; height: 800px; overflow: hidden; }
  body {
    background: var(--stage);
    font-family: "Montserrat", Arial, sans-serif;
    display: flex;
    align-items: center;
    justify-content: center;
    gap: 50px;
  }
  .card {
    position: relative;
    width: 525px;
    height: 300px;
    overflow: hidden;
  }
  /* Front */
  .card--front { background: var(--card-white); color: var(--ink); }
  .brand {
    position: absolute;
    top: 70px;
    right: 60px;
    text-align: right;
  }
  .brand__name {
    font-size: 30px;
    font-weight: 500;
    color: var(--ink);
    letter-spacing: 0.5px;
  }
  .brand__tagline {
    margin-top: 4px;
    font-size: 10px;
    color: var(--ink-soft);
  }
  .rule {
    position: absolute;
    left: 40px;
    right: 30px;
    top: 190px;
    height: 1px;
    background: var(--rule);
  }
  .person {
    position: absolute;
    left: 40px;
    bottom: 116px;
  }
  .person__name {
    font-size: 17px;
    font-weight: 700;
    letter-spacing: 0.3px;
    color: var(--ink);
  }
  .person__role {
    font-size: 12px;
    color: var(--accent);
    margin-top: 1px;
  }
  .contacts {
    position: absolute;
    left: 40px;
    top: 202px;
    list-style: none;
    font-size: 11.5px;
    color: var(--ink);
    line-height: 18px;
  }
  .contacts li { display: flex; align-items: center; gap: 8px; }
  .contacts svg { width: 11px; height: 11px; flex: none; }
  .address {
    position: absolute;
    right: 30px;
    top: 202px;
    text-align: right;
    font-size: 11.5px;
    line-height: 17px;
    color: var(--ink);
    font-style: normal;
  }
  .band {
    position: absolute;
    left: 0; right: 0; bottom: 0;
    height: 12px;
    display: flex;
  }
  .band__dark { flex: 0 0 60%; background: var(--band-dark); }
  .band__peach { flex: 1; background: var(--peach); }
  /* Back */
  .card--back {
    background: var(--card-grey);
    display: flex;
    flex-direction: column;
    align-items: center;
    justify-content: center;
  }
  .card--back .brand__name { color: var(--silver); font-size: 40px; }
  .card--back .brand__tagline { color: var(--silver); font-size: 13px; margin-top: 6px; }
</style>
</head>
<body>
  <section class="card card--front" aria-label="Fronte del biglietto">
    <div class="brand">
      <div class="brand__name">Lieve Cucina</div>
      <div class="brand__tagline">sapore leggero ogni giorno</div>
    </div>
    <div class="person">
      <div class="person__name">LUCA FERRI</div>
      <div class="person__role">President</div>
    </div>
    <div class="rule"></div>
    <ul class="contacts">
      <li>
        <svg viewBox="0 0 12 12" aria-hidden="true"><path d="M2.5 1 4.5 1 5.2 3.6 4 4.6C4.7 6 6 7.3 7.4 8L8.4 6.8 11 7.5 11 9.5C11 10.3 10.3 11 9.5 11 5 11 1 7 1 2.5 1 1.7 1.7 1 2.5 1Z" fill="var(--accent)"/></svg>
        321.654.0987
      </li>
      <li>
        <svg viewBox="0 0 12 12" aria-hidden="true"><rect x="0.5" y="2" width="11" height="8" fill="var(--accent)"/><path d="M0.5 2.5 6 6.5 11.5 2.5" fill="none" stroke="#fff" stroke-width="1"/></svg>
        info@piattileggerinuovi.it
      </li>
      <li>
        <svg viewBox="0 0 12 12" aria-hidden="true"><circle cx="6" cy="6" r="5" fill="none" stroke="var(--accent)" stroke-width="1.4"/></svg>
        @velusport72
      </li>
    </ul>
    <address class="address">
      1420 Willow Court<br>
      Juneau, Alaska 99801<br>
      piattileggerinuovi.it
    </address>
    <div class="band">
      <div class="band__dark"></div>
      <div class="band__peach"></div>
    </div>
  </section>

  <section class="card card--back" aria-label="Retro del biglietto">
    <div class="brand__name">Lieve Cucina</div>
    <div class="brand__tagline">sapore leggero ogni giorno</div>
  </section>
</body>
</html>
```